North Fern Holdings Business Card

A business card design to accompany the logo design you completed on Artisan Hive. We are open to your proposals. I did add one idea below that might work, but we aren't married to the idea. The company is a real estate services company. Clientele are typically high net worth individuals, executive level employment or owners of their own company, 30-60 years old.

Our 1 (bad?) idea: double sided card; One side landscape with logo and word mark. Other side Portrait with the logo only (oversize watermark maybe?). Somewhere add text of Name (Marcus Pellington), Title (Principal), phone # (949-555-0173) and email address (marcus@northfernhq.com). There would be a second design with my wife's name, number and email in place of mine.

Again totally open to ideas here.

Industry/Entity Type

Real Estate

```html
<!DOCTYPE html>
<html lang="en">
<head>
<meta charset="utf-8">
<title>North Fern Holdings — Business Card</title>
<link rel="stylesheet" href="https://fonts.googleapis.com/css2?family=Quicksand:wght@500;700&display=swap">
<style>
  :root {
    --backdrop: #e3e6e8;
    --card: #fbfbfa;
    --fern-green: #3a8a4e;
    --contact-coral: #e0603a;
    --card-shadow: rgba(40, 50, 55, 0.18);
  }
  * { margin: 0; padding: 0; box-sizing: border-box; }
  html, body {
    width: 1200px;
    height: 1127px;
    overflow: hidden;
    background: var(--backdrop);
    font-family: "Quicksand", sans-serif;
  }
  .canvas {
    position: relative;
    width: 1200px;
    height: 1127px;
  }
  .card {
    position: absolute;
    background: var(--card);
    box-shadow: 0 6px 14px var(--card-shadow);
  }
  .card--contact {
    left: 258px;
    top: 280px;
    width: 680px;
    height: 268px;
  }
  .contact-block {
    position: absolute;
    left: 46px;
    top: 86px;
    width: 265px;
    text-align: center;
  }
  .contact-name {
    font-weight: 700;
    font-size: 22px;
    letter-spacing: 0.5px;
    color: var(--fern-green);
  }
  .contact-title {
    font-weight: 500;
    font-size: 22px;
    color: var(--fern-green);
    margin-top: 2px;
  }
  .contact-details {
    margin-top: 42px;
    font-weight: 500;
    color: var(--contact-coral);
    line-height: 1.25;
  }
  .contact-phone { font-size: 18px; }
  .contact-email { font-size: 16px; }

  .card--brand {
    left: 238px;
    top: 578px;
    width: 752px;
    height: 332px;
    border: 7px solid var(--fern-green);
  }
  .brand-lockup {
    position: absolute;
    left: 90px;
    top: 92px;
    display: flex;
    align-items: center;
    gap: 38px;
  }
  .brand-mark {
    width: 118px;
    height: 118px;
    border-radius: 50%;
    background: var(--fern-green);
  }
  .brand-name {
    font-weight: 700;
    font-size: 44px;
    letter-spacing: 1px;
    color: var(--fern-green);
    line-height: 1.1;
  }
</style>
</head>
<body>
  <main class="canvas">
    <section class="card card--contact" aria-label="Card back with contact details">
      <div class="contact-block">
        <p class="contact-name">Marcus Pellington</p>
        <p class="contact-title">Principal</p>
        <div class="contact-details">
          <p class="contact-phone">949-555-0173</p>
          <p class="contact-email">marcus@northfernhq.com</p>
        </div>
      </div>
    </section>

    <section class="card card--brand" aria-label="Card front with company name">
      <div class="brand-lockup">
        <span class="brand-mark" aria-hidden="true"></span>
        <p class="brand-name">North Fern Holdings</p>
      </div>
    </section>
  </main>
</body>
</html>
```